Talvick Industrial Maintenance Business Card

Design a business card with the following information, logo must be included.
Talvick Industrial Maintenance
Dan Pelfrey Jr.
Pone 555-214-7608
email dan.pelfrey.jr@mailvantor.com

```html
<!DOCTYPE html>
<html lang="en">
<head>
<meta charset="utf-8">
<title>Talvick Industrial Maintenance – Business Card</title>
<link href="https://fonts.googleapis.com/css2?family=Montserrat:wght@400;500;700;800&display=swap" rel="stylesheet">
<style>
  :root {
    --navy: #1f3a6e;
    --navy-deep: #1a3262;
    --brand-blue: #1a6fc4;
    --faint-blue: #c8d2ec;
    --faint-navy: #223f77;
    --ink: #2b2b2b;
    --gray: #8a8a8a;
    --paper: #ffffff;
    --backdrop: #e9ebef;
  }
  * { box-sizing: border-box; margin: 0; padding: 0; }
  html, body {
    width: 1200px; height: 1186px; overflow: hidden;
    background: var(--backdrop);
    font-family: "Montserrat", sans-serif;
  }
  .stage {
    position: relative; width: 1200px; height: 1186px;
    display: flex; flex-direction: column; align-items: center; justify-content: center; gap: 60px;
  }
  .card {
    position: relative; width: 880px; height: 503px;
    border-radius: 26px; overflow: hidden;
    box-shadow: 0 10px 28px rgba(0,0,0,0.18);
  }
  /* Back side */
  .card--back { background: var(--navy); }
  .card--back .mark-decor {
    position: absolute; left: -120px; top: 90px;
    width: 430px; height: 430px; border-radius: 50%;
    background: var(--faint-navy);
    box-shadow: inset 0 0 0 2px rgba(0,0,0,0.12);
  }
  .card--back .wordmark {
    position: absolute; right: 70px; bottom: 150px;
    text-align: left; color: var(--brand-blue); font-weight: 800;
  }
  .wordmark .wordmark-main { display: block; font-size: 62px; letter-spacing: 1px; line-height: 1; }
  .wordmark .wordmark-sub { display: block; font-size: 15.5px; letter-spacing: 0.6px; margin-top: 4px; }

  /* Front side */
  .card--front { background: var(--paper); }
  .card--front .mark-decor {
    position: absolute; right: -150px; top: -40px;
    width: 420px; height: 420px; border-radius: 50%;
    background: var(--faint-blue);
  }
  .card--front .logo-lockup {
    position: absolute; left: 60px; top: 60px;
    display: flex; align-items: center; gap: 18px;
    color: var(--brand-blue); font-weight: 800;
  }
  .logo-lockup .logo-dot {
    width: 96px; height: 96px; border-radius: 50%; background: var(--brand-blue); flex: none;
  }
  .logo-lockup .wordmark-main { display: block; font-size: 56px; line-height: 1; letter-spacing: 1px; }
  .logo-lockup .wordmark-sub { display: block; font-size: 14px; letter-spacing: 0.6px; margin-top: 4px; }

  .contact {
    position: absolute; left: 60px; bottom: 50px; color: var(--ink);
  }
  .contact .person-name { color: var(--brand-blue); font-weight: 800; font-size: 30px; line-height: 1.1; }
  .contact .person-role { font-size: 18px; font-weight: 500; margin-top: 4px; }
  .contact .rule { width: 34px; height: 3px; background: var(--brand-blue); margin: 12px 0 16px; }
  .contact .line { display: flex; align-items: center; gap: 12px; font-size: 19px; font-weight: 500; margin-top: 8px; }
  .contact .icon {
    width: 24px; height: 24px; border-radius: 50%; background: var(--brand-blue);
    display: flex; align-items: center; justify-content: center; flex: none;
  }
</style>
</head>
<body>
<main class="stage">
  <section class="card card--back" aria-label="Card back">
    <div class="mark-decor" role="img" aria-label="Embossed company emblem area"></div>
    <div class="wordmark">
      <span class="wordmark-main">TALVICK</span>
      <span class="wordmark-sub">INDUSTRIAL MAINTENANCE</span>
    </div>
  </section>

  <section class="card card--front" aria-label="Card front">
    <div class="mark-decor" role="img" aria-label="Faint company emblem area"></div>
    <div class="logo-lockup">
      <span class="logo-dot"></span>
      <div>
        <span class="wordmark-main">TALVICK</span>
        <span class="wordmark-sub">INDUSTRIAL MAINTENANCE</span>
      </div>
    </div>
    <div class="contact">
      <p class="person-name">Dan Pelfrey Jr.</p>
      <p class="person-role">CEO &amp; Founder</p>
      <div class="rule"></div>
      <p class="line">
        <span class="icon">
          <svg width="13" height="13" viewBox="0 0 24 24" aria-hidden="true"><path fill="#fff" d="M6.6 10.8a15.1 15.1 0 0 0 6.6 6.6l2.2-2.2a1 1 0 0 1 1-.25 11.4 11.4 0 0 0 3.6.57 1 1 0 0 1 1 1V20a1 1 0 0 1-1 1A17 17 0 0 1 3 4a1 1 0 0 1 1-1h3.5a1 1 0 0 1 1 1c0 1.25.2 2.45.57 3.6a1 1 0 0 1-.25 1z"/></svg>
        </span>
        555-214-7608
      </p>
      <p class="line">
        <span class="icon">
          <svg width="13" height="13" viewBox="0 0 24 24" aria-hidden="true"><path fill="#fff" d="M3 6h18v12H3z"/><path fill="none" stroke="#1a6fc4" stroke-width="2" d="M3 6l9 7 9-7"/></svg>
        </span>
        dan.pelfrey.jr@mailvantor.com
      </p>
    </div>
  </section>
</main>
</body>
</html>
```